Business cards Dör Kornhüüs GmbH & Co.KG

We need a uniform business card design template for our employees.
A template should be created to have the same design for all business cards.

Contact Information for Business Card

Firma und Firmierung, Name, Funktion in Unternehmen, Anschrift, Tel. Handynummer, Emailadresse, Internetseite

Colors

Designer to choose colors to be used in the design.

Requirements
Must have
• Our company logo must be on it

```html
<!DOCTYPE html>
<html lang="de">
<head>
<meta charset="utf-8">
<title>Dör Kornhüüs – Visitenkarten</title>
<link href="https://fonts.googleapis.com/css2?family=Cormorant+Garamond:wght@500&family=Jost:wght@400&display=swap" rel="stylesheet">
<style>
  :root {
    --backdrop: #a8adad;
    --paper: #f5f4f1;
    --accent-red: #e23a55;
    --accent-purple: #a56bbb;
    --ink: #2b2b2b;
  }
  * { margin: 0; padding: 0; box-sizing: border-box; }
  html, body { width: 1200px; height: 824px; overflow: hidden; }
  body {
    background: var(--backdrop);
    position: relative;
    font-family: "Jost", sans-serif;
  }
  .card {
    position: absolute;
    background: var(--paper);
    border-radius: 3px;
  }
  .card--contact {
    left: 170px; top: 162px;
    width: 300px; height: 500px;
    border-bottom: 4px solid var(--accent-purple);
    text-align: center;
  }
  .card--brand {
    left: 540px; top: 262px;
    width: 500px; height: 300px;
    border-bottom: 4px solid var(--accent-purple);
    display: flex; align-items: center; justify-content: center;
  }
  .person-name {
    margin-top: 190px;
    font-family: "Cormorant Garamond", serif;
    font-weight: 500;
    font-size: 21px;
    letter-spacing: 0.5px;
    color: var(--accent-red);
    text-transform: uppercase;
  }
  .person-role {
    font-size: 13px;
    color: var(--accent-purple);
    margin-top: 2px;
  }
  .contact-icons {
    display: flex; justify-content: center; gap: 6px;
    margin: 14px 0 14px;
  }
  .contact-icons svg { width: 18px; height: 18px; }
  .contact-line {
    font-size: 14px;
    line-height: 18px;
    color: var(--ink);
  }
  .brand-name {
    font-family: "Cormorant Garamond", serif;
    font-weight: 500;
    font-size: 40px;
    letter-spacing: 1px;
    color: var(--accent-red);
    text-transform: uppercase;
  }
</style>
</head>
<body>
  <section class="card card--contact">
    <p class="person-name">Jonas Feldmann</p>
    <p class="person-role">President</p>
    <div class="contact-icons">
      <svg viewBox="0 0 18 18" aria-label="Telefon"><circle cx="9" cy="9" r="9" fill="var(--accent-purple)"/><path d="M6 5.2l1.6-.3.8 2-1 .8a5 5 0 0 0 2.9 2.9l.8-1 2 .8-.3 1.6c-3.8.4-7.2-3-6.8-6.8z" fill="#fff"/></svg>
      <svg viewBox="0 0 18 18" aria-label="E-Mail"><circle cx="9" cy="9" r="9" fill="var(--accent-purple)"/><rect x="5" y="6" width="8" height="6" fill="none" stroke="#fff" stroke-width="1"/><path d="M5 6l4 3.2L13 6" fill="none" stroke="#fff" stroke-width="1"/></svg>
      <svg viewBox="0 0 18 18" aria-label="Web"><circle cx="9" cy="9" r="9" fill="var(--accent-purple)"/><circle cx="9" cy="9" r="4.2" fill="none" stroke="#fff" stroke-width="1"/><path d="M4.8 9h8.4M9 4.8c-2 2.4-2 6 0 8.4M9 4.8c2 2.4 2 6 0 8.4" fill="none" stroke="#fff" stroke-width="0.8"/></svg>
    </div>
    <p class="contact-line">369.555.0142</p>
    <p class="contact-line">info@doerkornhuues.com</p>
    <p class="contact-line">doerkornhuues.com</p>
  </section>

  <section class="card card--brand">
    <p class="brand-name">Dör Kornhüüs</p>
  </section>
</body>
</html>
```